Want to learn how to safely prescribe Testosterone, bio-identical hormones and become an expert? I can teach you in 1 weekend!
I have developed and designed Vital Prime Clinic: the worlds first complete Anti-Aging Medical Platform with a "one-stop-learn-workshop tier" where a medical provider can attend my 3-Day Modern Renewal Practice Intensive Course.
During the 3 days the medical provider will become an expert in:
1. Identifying, stratifying and qualifying the appropriate patient for the anti-age hormonal protocol
2. Prescribing Testosterone, Estrogen, Progesterone, Dhea, HcG HgH, both men and women, when appropriate, using my unique and proprietary medically supervised hormone optimization protocol (the protocol as long as my hormone book will be made available to all course attendants)
3. Understanding nutraceuticals and recommending them when appropriate. PeakNovaMIX, the most perfectly developed multi-vitamin, mineral and anti-oxidant pack on the market will be made available for all course attendants to try for free
4. Prescribing a complete and powerful medically optimized weight loss program backed by my proprietary medically supervised protocol and published book (both the protocol and book are available free to all course attendants)
5. Understanding the exercise challenge and understanding what kind of exercise should be prescribed, to whom and in what form. (an extensive proprietary video exercise video library will be available for all course attendants)
6. Upon completion of the workshop each attendee will be proficient enough that upon return to his/her office on Monday, he/she will be able to greatly increase his/her revenue with the knowledge learned.
7. Upon request, the attendee can remain on as affiliate physician of Vital Prime Clinic and learn directly from Dr Varoszny who will help manage each affiliate physician's n.patient until the affiliate physician is confident enough on his/her own

The course will be held on a Saturday and Sunday in Hollywood Florida at the Seabrook Hotel in sunny South Florida

The Course will begin at 930am and end at 3pm each day allowing ample time for sun and fun

I want the email to be STUNNING , to catch the eye of the doctor as this is who I will be sending it to, I want the doctor who opens this email to NOT trash it, to be hypnotized by it, to be intrigued by it, to go ahead and book this course!!!

I will include the logos of Vital Prime Clinic, PeakNovaMix and my weight loss book

Please keep in mind this email MUST be stunning!!! It will be emailed blindly solely to physicians who are notoriously busy and usually trash unknown emails.

I also need to be able to edit the template

Target Market(s)

Doctors

Industry/Entity Type

Medical

Font styles to use
Serif
Sans Serif
Decorative
Script

Colors

Designer to choose colors to be used in the design.

Requirements
Must have
• Stunning colors
• Catchy fonts
• Cool graphics
Nice to have
• an email that is not easily deleted!
• an email that hypnotizes the doctor
• an email that tells the doctor "this is the course I must take!!"
• and email that tells the doctor "if I dont take this course I am a fool"
Should not have
• Negative connotations

```html
<!DOCTYPE html>
<html lang="en">
<head>
<meta charset="utf-8">
<title>Vital Prime Clinic – Weekend Hormone Workshop</title>
<link rel="stylesheet" href="https://fonts.googleapis.com/css2?family=Raleway:ital,wght@0,300;0,400;0,500;0,600;0,700;1,400&family=Dancing+Script:wght@600&display=swap">
<style>
:root{
  --red:#ee1c25;
  --dark:#333333;
  --darker:#2a2a2a;
  --page:#f4f4f4;
  --backdrop:#d6d6d6;
  --text:#444444;
  --muted:#666666;
  --icon:#8a8a8a;
  --white:#ffffff;
}
*{margin:0;padding:0;box-sizing:border-box}
html,body{width:1200px;height:2211px;overflow:hidden}
body{background:var(--backdrop);font-family:"Raleway",sans-serif;position:relative;color:var(--text)}
.email{position:absolute;left:226px;top:94px;width:750px;height:2023px;background:var(--page);border-top:5px solid var(--red);box-shadow:0 4px 18px rgba(0,0,0,.18)}
.abs{position:absolute}

.brand{left:33px;top:50px;font-size:31px;font-weight:500;color:var(--red);display:flex;align-items:center;gap:12px}
.brand .dot{width:20px;height:20px;border-radius:50%;background:var(--red)}
.social{left:602px;top:52px;display:flex;gap:4px}
.social span{width:33px;height:33px;display:block;border-radius:2px}
.social .s1{background:#3b5998}.social .s2{background:#1da1f2}.social .s3{background:var(--red)}

.hero{left:29px;top:140px;width:688px;height:325px;overflow:hidden;background:var(--dark);border-radius:3px}
.hero-photo{position:absolute;inset:0;
  background:
    radial-gradient(ellipse 22% 40% at 62% 30%,rgba(240,243,246,.95),transparent 70%),
    radial-gradient(ellipse 20% 45% at 88% 40%,rgba(250,250,252,.95),transparent 70%),
    radial-gradient(ellipse 25% 35% at 50% 85%,rgba(64,108,176,.75),transparent 70%),
    radial-gradient(ellipse 18% 30% at 78% 80%,rgba(208,214,222,.9),transparent 70%),
    linear-gradient(120deg,#9aa6b2,#dfe4e9 45%,#c4ccd4 75%,#8e99a4);
  clip-path:polygon(63% 0,100% 0,100% 100%,34% 100%)}
.hero-copy{position:absolute;left:34px;top:62px;width:258px;color:var(--white);font-size:19.5px;line-height:30px;font-weight:500}
.btn{background:var(--red);color:var(--white);font-weight:700;display:flex;align-items:center;justify-content:center;border-radius:2px}
.hero-btn{left:34px;top:232px;width:293px;height:51px;font-size:17.5px}

.author-card{left:30px;top:524px;width:174px;height:197px;background:var(--white);border:1px solid #ddd;overflow:hidden}
.author-card .red{position:absolute;inset:0;background:var(--red);clip-path:polygon(0 0,52% 0,20% 100%,0 100%)}
.author-card .portrait{position:absolute;left:8px;top:18px;width:158px;height:158px;border-radius:50%;border:6px solid #e5e5e5;background:radial-gradient(circle at 50% 38%,#e0b89c 0,#d4a98c 22%,transparent 36%),radial-gradient(ellipse 60% 40% at 50% 95%,#cfd8e4,transparent 70%),linear-gradient(180deg,#eef0f2,#dfe3e6)}
.signature{left:30px;top:736px;width:174px;text-align:center;font-family:"Dancing Script",cursive;color:var(--red);font-size:17px}
.intro{left:229px;top:548px;width:494px;font-size:16.5px;line-height:27.5px;color:var(--muted);font-weight:400}
.intro .tier{color:var(--red);font-weight:700;font-size:22px}
.intro-btn{left:231px;top:711px;width:363px;height:57px;font-size:17.5px;gap:10px}

.team{left:44px;top:835px;width:681px;height:265px;
  background:
    radial-gradient(ellipse 6% 22% at 10% 60%,rgba(40,110,200,.55),transparent 70%),
    radial-gradient(ellipse 6% 22% at 86% 60%,rgba(40,110,200,.55),transparent 70%),
    radial-gradient(ellipse 50% 30% at 50% 18%,rgba(170,150,140,.35),transparent 70%),
    linear-gradient(180deg,#c9cfd6 0,#e9ecef 30%,#f7f8f9 70%,#eceff2 100%);
  clip-path:polygon(0 8%,100% 6%,100% 100%,0 100%)}
.schedule{left:94px;top:969px;width:562px;height:169px;background:var(--white);border:1px solid #ddd;overflow:hidden}
.schedule .corner{position:absolute;right:0;top:0;width:150px;height:100%;background:var(--red);clip-path:polygon(42% 0,100% 0,100% 100%,0 100%)}
.schedule .clock{position:absolute;right:24px;top:47px}
.schedule h2{position:absolute;left:0;width:430px;top:20px;text-align:center;color:var(--red);font-size:29px;font-weight:700}
.schedule p{position:absolute;left:20px;width:398px;top:77px;text-align:center;font-size:18px;line-height:25px;color:var(--text)}

.expert-title{left:0;width:750px;top:1193px;text-align:center;color:var(--red);font-size:25px;font-weight:600;line-height:31px}
.skill{width:240px;text-align:center}
.skill svg{display:block;margin:0 auto}
.skill p{margin-top:22px;font-style:italic;font-size:18px;line-height:24px;color:var(--muted)}

.cta{left:29px;top:1681px;width:688px;height:74px;background:var(--red)}
.cta p{position:absolute;left:60px;top:24px;color:var(--white);font-weight:700;font-size:18px}
.cta .contact-btn{position:absolute;left:456px;top:10px;width:175px;height:53px;background:var(--white);color:var(--red);font-weight:700;font-size:16px;display:flex;align-items:center;justify-content:center;border-radius:3px}

.footer{left:0;top:1781px;width:750px;height:242px;background:var(--darker);overflow:hidden}
.footer .panel{position:absolute;inset:0;background:#3d3d3d;clip-path:polygon(0 0,68% 0,47% 100%,0 100%)}
.contact-line{position:absolute;left:76px;color:#d5d5d5;font-size:16px}
.contact-line.bold{font-weight:700;line-height:25px}
.ficon{position:absolute;left:36px}
.fsocial{left:451px;top:63px;display:flex;gap:6px}
.fsocial span{width:34px;height:34px;border-radius:50%;border:2px solid #bdbdbd;display:block}
.fbrand{left:451px;top:110px;color:#bdbdbd;font-size:18px;font-weight:500}
.copyright{left:451px;top:155px;color:var(--red);font-size:17px;font-weight:500}
</style>
</head>
<body>
<main class="email">
  <div class="abs brand"><span>Vital Prime Clinic</span><span class="dot"></span></div>
  <div class="abs social" aria-label="Social links"><span class="s1"></span><span class="s2"></span><span class="s3"></span></div>

  <section class="abs hero">
    <div class="hero-photo" role="img" aria-label="Photo of a team of doctors in white coats reviewing a tablet"></div>
    <p class="hero-copy">Want to learn how to safely prescribe Testosterone, bio-identical hormones and become an expert?</p>
    <a class="abs btn hero-btn">I can teach you in 1 weekend!</a>
  </section>

  <div class="abs author-card"><div class="red"></div><div class="portrait" role="img" aria-label="Portrait photo of the course doctor"></div></div>
  <p class="abs signature">Dr. Marek Varoszny MD</p>
  <p class="abs intro">I have developed and designed Vital Prime Clinic: the worlds first complete Anti-Aging Medical Platform with a<br><span class="tier">"one-stop-learn-workshop tier"</span> where a medical provider can attend my 3-Day Modern Renewal Practice Intensive Course.</p>
  <a class="abs btn intro-btn">Come My Website to Know More
    <svg width="14" height="14" viewBox="0 0 14 14" fill="none" stroke="#fff" stroke-width="2"><path d="M2 2l5 5-5 5M7 2l5 5-5 5"/></svg></a>

  <div class="abs team" role="img" aria-label="Photo of a row of medical staff in white coats"></div>
  <section class="abs schedule">
    <div class="corner"></div>
    <svg class="clock" width="74" height="74" viewBox="0 0 74 74" fill="none" stroke="#fff" stroke-width="5"><circle cx="37" cy="37" r="32"/><path d="M37 18v20l-10 10" stroke-linecap="round"/></svg>
    <h2>9:30am a- 3:00pm</h2>
    <p>The course will be held on a Saturday and Sunday in Hollywood Florida at the Seabrook Hotel in sunny South Florida</p>
  </section>

  <h2 class="abs expert-title">During the 3 days the medical provider<br>will become an expert in:</h2>

  <div class="abs skill" style="left:20px;top:1318px">
    <svg width="66" height="66" viewBox="0 0 66 66" fill="var(--icon)"><rect x="14" y="8" width="38" height="52" rx="4"/><rect x="24" y="3" width="18" height="10" rx="3"/><rect x="21" y="22" width="24" height="4" fill="#f4f4f4"/><rect x="21" y="32" width="24" height="4" fill="#f4f4f4"/><rect x="21" y="42" width="16" height="4" fill="#f4f4f4"/></svg>
    <p>Identifying perfect<br>patients</p></div>
  <div class="abs skill" style="left:248px;top:1318px">
    <svg width="66" height="66" viewBox="0 0 66 66" fill="var(--icon)"><rect x="10" y="6" width="38" height="50" rx="3"/><rect x="17" y="16" width="24" height="4" fill="#f4f4f4"/><rect x="17" y="25" width="24" height="4" fill="#f4f4f4"/><rect x="17" y="34" width="14" height="4" fill="#f4f4f4"/><g transform="rotate(-40 46 48)"><rect x="32" y="41" width="28" height="14" rx="7" stroke="#f4f4f4" stroke-width="3"/></g></svg>
    <p>Prescribe appropriate<br>medicine.</p></div>
  <div class="abs skill" style="left:475px;top:1318px">
    <svg width="66" height="66" viewBox="0 0 66 66" fill="var(--icon)"><rect x="24" y="4" width="18" height="9" rx="2"/><path d="M20 16h26l4 8v34a4 4 0 0 1-4 4H20a4 4 0 0 1-4-4V24z"/><rect x="22" y="32" width="22" height="14" rx="2" fill="#f4f4f4"/></svg>
    <p>Provide additives<br>nutraceuticals if needs</p></div>
  <div class="abs skill" style="left:20px;top:1494px">
    <svg width="66" height="66" viewBox="0 0 66 66" fill="none" stroke="var(--icon)" stroke-width="4"><rect x="6" y="8" width="54" height="54" rx="8"/><circle cx="33" cy="20" r="7"/><path d="M33 20l3-4"/><ellipse cx="23" cy="44" rx="5" ry="8" fill="var(--icon)"/><ellipse cx="43" cy="44" rx="5" ry="8" fill="var(--icon)"/></svg>
    <p>Knowledge about<br>weight loss program</p></div>
  <div class="abs skill" style="left:248px;top:1494px">
    <svg width="66" height="66" viewBox="0 0 66 66" fill="var(--icon)"><rect x="4" y="22" width="8" height="22" rx="2"/><rect x="13" y="16" width="9" height="34" rx="2"/><rect x="22" y="30" width="22" height="6"/><rect x="44" y="16" width="9" height="34" rx="2"/><rect x="54" y="22" width="8" height="22" rx="2"/></svg>
    <p>Understanding vast<br>knowledge about excercise</p></div>
  <div class="abs skill" style="left:475px;top:1494px">
    <svg width="66" height="66" viewBox="0 0 66 66" fill="none" stroke="var(--icon)" stroke-width="4" stroke-linecap="round"><path d="M16 6v16a12 12 0 0 0 24 0V6"/><path d="M28 34v10a10 10 0 0 0 20 0v-8"/><circle cx="48" cy="30" r="6" fill="var(--icon)"/></svg>
    <p>Direct Dr Varoszny<br>practice sessions</p></div>

  <section class="abs cta">
    <p>Enroll Today! Contact us for more information</p>
    <a class="contact-btn">CONTRACT NOW</a>
  </section>

  <footer class="abs footer">
    <div class="panel"></div>
    <svg class="ficon" style="top:44px" width="20" height="20" viewBox="0 0 20 20" fill="#9a9a9a"><path d="M4 1l4 4-2 3c1 3 3 5 6 6l3-2 4 4-3 3C8 19 1 12 1 4z"/></svg>
    <p class="contact-line" style="top:44px">555-214-0381</p>
    <p class="contact-line" style="top:74px">555-218-7704</p>
    <svg class="ficon" style="top:106px" width="26" height="18" viewBox="0 0 26 18" fill="none" stroke="#9a9a9a" stroke-width="1.6"><rect x="1" y="1" width="24" height="16"/><path d="M1 1l12 9 12-9"/></svg>
    <p class="contact-line" style="top:104px">hello@vitalprimeclinic.example</p>
    <svg class="ficon" style="top:140px" width="22" height="30" viewBox="0 0 22 30" fill="#9a9a9a"><path d="M11 0a11 11 0 0 0-11 11c0 8 11 19 11 19s11-11 11-19A11 11 0 0 0 11 0zm0 15a4 4 0 1 1 0-8 4 4 0 0 1 0 8z"/></svg>
    <p class="contact-line bold" style="top:134px">820 Palmetto Grove Ave,<br>Coral Shore FL 33100</p>
    <div class="abs fsocial" aria-label="Social links"><span></span><span></span><span></span></div>
    <p class="abs fbrand">Vital Prime Clinic</p>
    <p class="abs copyright">© 2017 Vital Prime Clinic.</p>
  </footer>
</main>
</body>
</html>
```